VelmaRin packaging label

I would like to have designs for a range of packaging labels for an 100% organic skincare and cosmetics product range. The designer will first need to visit the following website and choose a packaging bottle or jar first and then design a "sticker" label which can stick onto the bottle or jars. I have attached the logo. The product is a luxury skincare product which focuses on 100% organic ingredients and putting the true glow back into people's skin.
http://shop.kestrelvane.example.au/epages/kestrelvane.sf/en_AU/?ObjectPath=/Shops/kestrelvane/Categories/16
The bottles and jars will be for 50ml and 100ml. I prefer the amber glass bottles for cleansers, toners and jars for moisturisers. Labels may include designs which can be sticked around the jar or bottles and onto the cap of the jar.
I particularly like "vintage designs" as it reflects the "luxury" status of the products. I also like "organic" designs. Please ensure the design sets my products apart from the rest and is eye catching when placed with other products on the shelfs.
I have attached some packaging samples which I really like. The sticker can be custom cut, rectangular, circle, oval in shape etc.
Please make the design editable (send me ai as well as editable pdf) so that I can put the names of the products eg toner, cleaner on it. You may choose to design a range of labels or 1-2 which can be used on every product.
Target Market(s)
High income working class and rich house wives.
Requirements
Must have
- Elegance
Please also use the similar design but for different sizes and products.
1. sticker labels for amber glass 50ml jar. For jar and round cap.
2. Sticker labels for 15 ml serum
3. 100 ml for amber glass toner and cleanser bottles.
Nice to have
- Eye catchy

```html
<!DOCTYPE html>
<html lang="en">
<head>
<meta charset="utf-8">
<title>VelmaRin Packaging Labels</title>
<link rel="stylesheet" href="https://fonts.googleapis.com/css2?family=Cinzel:wght@400&family=Lato:wght@400&display=swap">
<style>
  :root {
    --canvas-bg: #ffffff;
    --label-fill: #d3b5ab;
    --label-edge: #f3e1dd;
    --label-stitch: #fbf4f2;
    --label-ink: #ffffff;
  }
  * { margin: 0; padding: 0; box-sizing: border-box; }
  html, body { width: 1200px; height: 1000px; overflow: hidden; background: var(--canvas-bg); }
  .label-range { position: relative; width: 1200px; height: 1000px; }
  .label {
    position: absolute;
    width: 310px;
    height: 310px;
    transform-origin: top left;
  }
  .label--toner { left: 175px; top: 428px; }
  .label--cleanser { left: 500px; top: 428px; }
  .label--serum { left: 843px; top: 643px; transform: scale(0.5); }
  .label-shape { position: absolute; inset: 0; width: 100%; height: 100%; }
  .label-shape .edge { fill: var(--label-fill); stroke: var(--label-edge); stroke-width: 7; }
  .label-shape .stitch { fill: none; stroke: var(--label-stitch); stroke-width: 1.4; stroke-dasharray: 4 3; }
  .label-content {
    position: absolute; inset: 0;
    display: flex; flex-direction: column; align-items: center;
    color: var(--label-ink);
  }
  .brand-dot {
    margin-top: 58px;
    width: 42px; height: 42px;
    border-radius: 50%;
    background: var(--label-ink);
  }
  .brand-name {
    margin-top: 20px;
    font-family: 'Cinzel', serif;
    font-size: 38px;
    letter-spacing: 1px;
    line-height: 1;
  }
  .product-name {
    margin-top: 30px;
    font-family: 'Cinzel', serif;
    font-size: 19px;
    letter-spacing: 1px;
    line-height: 1;
  }
  .divider {
    margin-top: 10px;
    width: 160px; height: 10px;
  }
  .divider line { stroke: var(--label-ink); stroke-width: 1.2; }
  .divider circle { fill: var(--label-ink); }
  .volume {
    margin-top: 6px;
    font-family: 'Lato', sans-serif;
    font-size: 12px;
    line-height: 1;
  }
</style>
</head>
<body>
<svg width="0" height="0" style="position:absolute" aria-hidden="true">
  <defs>
    <path id="label-outline" d="M60,32 Q150,4 240,32 Q246,58 272,64 L305,155 L272,246 Q246,252 240,278 Q150,306 60,278 Q54,252 28,246 L5,155 L28,64 Q54,58 60,32 Z"/>
  </defs>
</svg>

<main class="label-range">
  <section class="label label--toner">
    <svg class="label-shape" viewBox="0 0 310 310" aria-hidden="true">
      <use href="#label-outline" class="edge"/>
      <use href="#label-outline" class="stitch" transform="translate(155 155) scale(0.88) translate(-155 -155)"/>
    </svg>
    <div class="label-content">
      <span class="brand-dot"></span>
      <p class="brand-name">VelmaRin</p>
      <p class="product-name">Toner</p>
      <svg class="divider" viewBox="0 0 160 10" aria-hidden="true">
        <circle cx="4" cy="5" r="2.5"/><line x1="8" y1="5" x2="152" y2="5"/><circle cx="80" cy="5" r="2"/><circle cx="156" cy="5" r="2.5"/>
      </svg>
      <p class="volume">100 mL</p>
    </div>
  </section>

  <section class="label label--cleanser">
    <svg class="label-shape" viewBox="0 0 310 310" aria-hidden="true">
      <use href="#label-outline" class="edge"/>
      <use href="#label-outline" class="stitch" transform="translate(155 155) scale(0.88) translate(-155 -155)"/>
    </svg>
    <div class="label-content">
      <span class="brand-dot"></span>
      <p class="brand-name">VelmaRin</p>
      <p class="product-name">Cleanser</p>
      <svg class="divider" viewBox="0 0 160 10" aria-hidden="true">
        <circle cx="4" cy="5" r="2.5"/><line x1="8" y1="5" x2="152" y2="5"/><circle cx="80" cy="5" r="2"/><circle cx="156" cy="5" r="2.5"/>
      </svg>
      <p class="volume">100 mL</p>
    </div>
  </section>

  <section class="label label--serum">
    <svg class="label-shape" viewBox="0 0 310 310" aria-hidden="true">
      <use href="#label-outline" class="edge"/>
      <use href="#label-outline" class="stitch" transform="translate(155 155) scale(0.88) translate(-155 -155)"/>
    </svg>
    <div class="label-content">
      <span class="brand-dot"></span>
      <p class="brand-name">VelmaRin</p>
      <p class="product-name">Serum</p>
      <svg class="divider" viewBox="0 0 160 10" aria-hidden="true">
        <circle cx="4" cy="5" r="2.5"/><line x1="8" y1="5" x2="152" y2="5"/><circle cx="80" cy="5" r="2"/><circle cx="156" cy="5" r="2.5"/>
      </svg>
      <p class="volume">15 mL</p>
    </div>
  </section>
</main>
</body>
</html>
```